Recreate a label for a champagne bottle [See attached example]

I'm needing to recreate a label for a champagne bottle label to give as closing gifts to clients when they purchase a home. Please include the following text "Welcome Home", my initials "R.T", "Established Year", the hashtag #BubbLORNE and my logo (attached). I prefer to have a black or white background with a crisp, easy to read cursive font similar to the Dunmore bourbon font. I want it to look as similar of a layout to the Valcorta label as possible

Target Market(s)

Luxury

Font styles to use
Decorative
Script

Colors

Designer to choose only greyscale colors for use in the design.

Requirements
Must have
• "Welcome Home", my initials "R.T", "Established Year", the hashtag #BubbLORNE and my logo
Nice to have
• Clean cursive font, easy to read, luxury look.
Should not have
• Clutter, too much design.

```html
<!DOCTYPE html>
<html lang="en">
<head>
<meta charset="utf-8">
<title>Welcome Home – Champagne Label</title>
<link href="https://fonts.googleapis.com/css2?family=Pinyon+Script&family=Montserrat:wght@600;700&display=swap" rel="stylesheet">
<style>
  :root {
    --backdrop: #38393b;
    --frame: #6b6b6f;
    --label: #232324;
    --silver: #d6d6d8;
    --gold-light: #f3e9c6;
    --gold-mid: #d8c48e;
    --gold-deep: #a88f55;
    --ink-dark: #1c1c1c;
  }
  * { margin: 0; padding: 0; box-sizing: border-box; }
  html, body {
    width: 1200px;
    height: 900px;
    overflow: hidden;
    background: var(--backdrop);
  }
  .canvas {
    position: relative;
    width: 1200px;
    height: 900px;
  }
  .label {
    position: absolute;
    left: 200px;
    top: 97px;
    width: 800px;
    height: 706px;
    background: var(--frame);
    padding: 28px;
  }
  .label-face {
    position: relative;
    width: 100%;
    height: 100%;
    background: var(--label);
    text-align: center;
  }
  .established {
    position: absolute;
    top: 62px;
    left: 0;
    right: 0;
    display: flex;
    justify-content: center;
    align-items: center;
    gap: 34px;
    font-family: "Montserrat", sans-serif;
    font-weight: 600;
    font-size: 20px;
    letter-spacing: 0.32em;
    color: var(--silver);
  }
  .brand-mark {
    display: flex;
    align-items: center;
    gap: 10px;
    letter-spacing: 0.12em;
  }
  .brand-mark .mark-square {
    width: 16px;
    height: 16px;
    background: var(--silver);
  }
  .greeting {
    position: absolute;
    top: 170px;
    left: 0;
    right: 0;
    font-family: "Pinyon Script", cursive;
    font-size: 132px;
    line-height: 0.78;
    background: linear-gradient(100deg, var(--gold-deep) 0%, var(--gold-light) 35%, var(--gold-mid) 60%, var(--gold-light) 80%, var(--gold-deep) 100%);
    -webkit-background-clip: text;
    background-clip: text;
    color: transparent;
  }
  .greeting .line-one { display: block; margin-left: 20px; }
  .greeting .line-two { display: block; margin-left: -70px; }
  .initials {
    position: absolute;
    top: 490px;
    left: 0;
    right: 0;
    font-family: "Montserrat", sans-serif;
    font-weight: 700;
    font-size: 40px;
    letter-spacing: 0.28em;
    color: var(--silver);
  }
  .hashtag {
    position: absolute;
    top: 572px;
    left: 202px;
    width: 400px;
    height: 50px;
    display: flex;
    align-items: center;
    justify-content: center;
    background: linear-gradient(90deg, var(--gold-deep) 0%, var(--gold-light) 45%, var(--gold-mid) 75%, var(--gold-deep) 100%);
    font-family: "Montserrat", sans-serif;
    font-weight: 700;
    font-size: 30px;
    letter-spacing: 0.16em;
    color: var(--ink-dark);
  }
</style>
</head>
<body>
  <div class="canvas">
    <div class="label">
      <div class="label-face">
        <div class="established">
          <span>ESTD</span>
          <span class="brand-mark"><span class="mark-square"></span>TARN ESTATES</span>
          <span>2023</span>
        </div>
        <h1 class="greeting">
          <span class="line-one">Welcome</span>
          <span class="line-two">Home</span>
        </h1>
        <p class="initials">R.T.</p>
        <p class="hashtag">#BubbLORNE</p>
      </div>
    </div>
  </div>
</body>
</html>
```